OLVAK Web Design (Need help to re-design our website)

We need someone to help us re-design our website and launch it. All contents for the website are ready. (https://olvak.example.au/)

-Rearrange categories:
1. Heating & Cooling
2. Remove Home Appliance
3. Remove Entertainment

Home page - redesign (It will be a nice touch if the banner is in the loop).

NOTE:
-Brand colour blue and orange.
-Try using professional fonts (Example: Helvetica, etc.)
-The website's Footer should be readable and use light colour.

Target Market(s)

Residentials & commercial buildings

Industry/Entity Type

Heat Ventilation and Cooling Industry, Technology , Renewables

Coding

Coded - Design and coding required

Colors
0094D4
00A9DD
6FCCEA
C7EBF8
E9F6FB
59FF00
82FF00
B8FF75
E3FFCB
F4FFEA
F0912C
F2A743
F7CA91
FBE8D2
FDF5EE

Requirements
Nice to have
• Effects/transition on the words/copy/images.

```html
<!DOCTYPE html>
<html lang="en">
<head>
<meta charset="utf-8">
<title>OLVAK – Heating and Cooling Services</title>
<link rel="stylesheet" href="https://fonts.googleapis.com/css2?family=Titillium+Web:wght@400;600;700&display=swap">
<style>
:root{
  --orange:#f7931e;
  --blue:#1166b3;
  --blue-deep:#0f5fae;
  --ink:#111;
  --grey-band:#d8d8d8;
  --footer:#040c16;
  --white:#fff;
  --muted:#c9d3de;
}
*{box-sizing:border-box;margin:0;padding:0}
html,body{width:1200px;height:2667px;overflow:hidden;background:var(--white);font-family:"Titillium Web",Helvetica,Arial,sans-serif;color:var(--ink)}
.page{position:relative;width:1200px;height:2667px}
.abs{position:absolute}
.topbar{left:0;top:0;width:1200px;height:33px;background:var(--orange);font-size:12px;font-weight:600}
.topbar .promo{left:77px;top:7px}
.topbar .promo u{margin-left:14px}
.topbar .contact{right:52px;top:8px;display:flex;gap:14px;align-items:center}
.header{left:0;top:33px;width:1200px;height:122px;background:var(--white)}
.brand{display:flex;align-items:center;gap:12px;color:var(--blue);font-weight:700;letter-spacing:6px}
.brand .mark{width:36px;height:36px;background:var(--orange)}
.header .brand{left:66px;top:38px;font-size:44px}
.search{left:722px;top:43px;width:185px;height:40px;background:#d6d6d6;display:flex;align-items:center;gap:8px;padding-left:12px;font-size:15px;font-weight:600}
.book{left:922px;top:43px;width:235px;height:40px;background:var(--blue);color:var(--white);font-size:15px;font-weight:600;letter-spacing:2px;display:flex;align-items:center;justify-content:center}
.nav{left:0;top:155px;width:1200px;height:46px;background:var(--blue);display:flex;color:var(--white);font-size:19px;font-weight:600}
.nav .item{display:flex;align-items:center;justify-content:center;gap:14px;border-right:1px solid rgba(255,255,255,.5)}
.nav .home{margin-left:75px;width:183px;background:var(--orange)}
.nav .hc{width:327px}.nav .story{width:264px}.nav .support{width:220px;border-right:0}
.nav i{display:inline-block;width:20px;height:14px;border:2px solid var(--white);border-radius:2px}
.hero{left:0;top:201px;width:1200px;height:452px;background:linear-gradient(100deg,#0a1620 0%,#14303e 40%,#2f5c6d 70%,#496f7c 100%)}
.hero .kicker{left:87px;top:120px;color:var(--white);font-size:12px}
.hero h1{left:85px;top:134px;color:var(--white);font-size:58px;font-weight:700;line-height:1.1}
.hero .sub{left:87px;top:206px;color:var(--white);font-size:22px;font-weight:600}
.btn-orange{background:var(--orange);color:var(--white);display:flex;align-items:center;justify-content:center}
.hero .explore{left:87px;top:254px;width:228px;height:41px;font-size:19px;letter-spacing:1.5px;font-weight:600}
.social{display:flex;gap:10px}
.social span{width:22px;height:22px;background:var(--white);border-radius:50%;opacity:.9}
.hero .social{left:87px;top:328px}
.hero .arrows{left:1078px;top:410px;display:flex;gap:18px}
.rebates{left:0;top:653px;width:1200px;height:243px;background:var(--grey-band)}
.rebates h2{left:0;width:1200px;top:25px;text-align:center;color:var(--blue);font-size:31px;font-weight:600}
.badge{width:130px;height:130px;border-radius:50%;top:87px}
.b1{left:356px;background:#2b3f8f}.b2{left:546px;background:#c99a2e}.b3{left:722px;background:#fff}
.section-title{left:0;width:1200px;text-align:center;color:var(--blue)}
.products-title{top:968px;font-size:33px;font-weight:600}
.products-sub{top:1010px;font-size:15px;font-weight:600}
.card{top:1071px;height:491px;border:1px solid #ddd;background:var(--white)}
.card .shot{position:absolute;left:50%;transform:translateX(-50%);background:linear-gradient(90deg,#9a9a9a,#e8e8e8 45%,#a8a8a8)}
.card .foot{position:absolute;left:0;bottom:0;width:100%;height:121px;background:var(--orange);color:var(--white);text-align:center}
.card .foot h3{font-size:23px;font-weight:600;margin-top:24px}
.card .foot .go{display:inline-block;margin-top:6px;width:94px;height:32px;line-height:32px;background:var(--blue);font-size:13px;letter-spacing:3px;font-weight:600}
.c1{left:82px;width:247px}.c2{left:353px;width:246px}.c3{left:617px;width:246px}.c4{left:877px;width:248px}
.cta{left:0;top:1596px;width:1200px;height:493px;background:var(--blue-deep);color:var(--white);text-align:center}
.cta .kicker{top:130px;width:1200px;font-size:12px}
.cta h2{top:146px;width:1200px;font-size:58px;font-weight:700}
.cta .sub{top:222px;width:1200px;font-size:22px;font-weight:600}
.cta .call{top:290px;width:1200px;font-size:25px;font-weight:600}
.cta .phone{left:406px;top:332px;width:387px;height:69px;font-size:47px;font-weight:600}
.footer{left:0;top:2089px;width:1200px;height:478px;background:var(--footer);color:var(--white)}
.footer .join{left:122px;top:78px;font-size:18px;font-weight:600;line-height:1.3}
.subscribe{left:803px;top:90px;width:322px;height:30px;background:#d9d9d9;display:flex;align-items:center;font-size:10px;color:#444;padding-left:10px}
.subscribe b{margin-left:auto;width:70px;height:26px;margin-right:2px;background:#e8202a;color:var(--white);font-weight:400;display:flex;align-items:center;justify-content:center}
.rule{left:122px;width:1003px;height:1px;background:#555}
.footer .brand{left:122px;top:183px;font-size:40px;color:var(--blue)}
.col{top:186px;font-size:10px;color:var(--muted);line-height:1.4}
.col h4{color:var(--blue);font-size:15px;font-weight:600;margin-bottom:8px}
.col li{list-style:none;margin-bottom:10px}
.contact-num{font-size:20px;color:var(--white)}
.copy{left:0;width:1200px;text-align:center;font-size:10px;color:var(--muted)}
</style>
</head>
<body>
<div class="page">

  <div class="abs topbar">
    <div class="abs promo">Don't miss our <u>Latest Promotions</u></div>
    <div class="abs contact">
      <span>Call Us &nbsp; 1800 555 014</span>
      <svg width="18" height="13" viewBox="0 0 18 13"><rect x="1" y="1" width="16" height="11" fill="none" stroke="#111" stroke-width="1.5"/><path d="M1 1l8 6 8-6" fill="none" stroke="#111" stroke-width="1.5"/></svg>
      <span>info@olvak.example.au</span>
    </div>
  </div>

  <header class="abs header">
    <div class="abs brand"><span class="mark"></span>OLVAK</div>
    <div class="abs search">
      <svg width="14" height="14" viewBox="0 0 14 14"><circle cx="5.5" cy="5.5" r="4.2" fill="none" stroke="#111" stroke-width="1.8"/><path d="M8.6 8.6L13 13" stroke="#111" stroke-width="1.8"/></svg>
      Search....
    </div>
    <div class="abs book">BOOK APPOINTMENT</div>
  </header>

  <nav class="abs nav">
    <div class="item home"><i></i>Home</div>
    <div class="item hc"><i></i>Heating and Cooling</div>
    <div class="item story"><i></i>Our Story</div>
    <div class="item support"><i></i>Support</div>
  </nav>

  <section class="abs hero" role="img" aria-label="Outdoor air conditioning units and ducting on a rooftop at dusk">
    <div class="abs kicker">EXPLORE OUR</div>
    <h1 class="abs">Heating and Cooling Services</h1>
    <div class="abs sub">Spend your four seasons with OLVAK</div>
    <div class="abs explore btn-orange">EXPLORE NOW</div>
    <div class="abs social" aria-label="Social links"><span></span><span></span><span></span></div>
    <div class="abs arrows">
      <svg width="18" height="16" viewBox="0 0 18 16"><path d="M17 8H2M8 1L1 8l7 7" fill="none" stroke="#fff" stroke-width="2"/></svg>
      <svg width="18" height="16" viewBox="0 0 18 16"><path d="M1 8h15M10 1l7 7-7 7" fill="none" stroke="#fff" stroke-width="2"/></svg>
    </div>
  </section>

  <section class="abs rebates">
    <h2 class="abs">Fully Compliant &nbsp;with all Government &nbsp;Rebates</h2>
    <div class="abs badge b1" role="img" aria-label="Locally owned badge"></div>
    <div class="abs badge b2" role="img" aria-label="Premium quality badge"></div>
    <div class="abs badge b3" role="img" aria-label="Energy saving badge"></div>
  </section>

  <h2 class="abs section-title products-title">Our Products</h2>
  <div class="abs section-title products-sub">You can Find best quality products here</div>

  <div class="abs card c1">
    <div class="shot" role="img" aria-label="Heat pump water heater" style="top:52px;width:86px;height:262px;border-radius:6px"></div>
    <div class="foot"><h3>Heat Pump</h3><span class="go">EXPLORE</span></div>
  </div>
  <div class="abs card c2">
    <div class="shot" role="img" aria-label="Split system air conditioner" style="top:142px;width:172px;height:58px;border-radius:6px;background:linear-gradient(#fafafa,#dcdcdc)"></div>
    <div class="foot"><h3>Air Conditioners</h3><span class="go">EXPLORE</span></div>
  </div>
  <div class="abs card c3">
    <div class="shot" role="img" aria-label="Tall heat pump water heater" style="top:32px;width:76px;height:305px;border-radius:6px"></div>
    <div class="foot"><h3 style="margin-top:18px">Air Conditioners</h3><span class="go">EXPLORE</span></div>
  </div>
  <div class="abs card c4">
    <div class="shot" role="img" aria-label="Monoblock outdoor heat pump unit" style="top:122px;width:172px;height:126px;background:linear-gradient(#f4f4f4,#d4d4d4)"></div>
    <div class="foot"><h3 style="margin-top:18px">Monoblock Heat Pump</h3><span class="go">EXPLORE</span></div>
  </div>

  <section class="abs cta">
    <div class="abs kicker">EXPLORE OUR</div>
    <h2 class="abs">Heating and Cooling Services</h2>
    <div class="abs sub">OLVAK IS HERE TO SOLVE YOUR ALL HEATING AND COOLING PROBLEMS</div>
    <div class="abs call">CALL NOW</div>
    <div class="abs phone btn-orange">(555) 210-4478</div>
  </section>

  <footer class="abs footer">
    <div class="abs join">JOIN OUR LIST TO GET THE LATEST<br>UPDATES FROM OLVAK</div>
    <div class="abs subscribe">Your Email Address<b>Subscribe</b></div>
    <div class="abs rule" style="top:149px"></div>
    <div class="abs brand"><span class="mark"></span>OLVAK</div>
    <div class="abs col" style="left:367px;width:150px">
      <h4>Our Mission</h4>
      <p>OLVAK is a comapny dedicated to manufacturing and installing energy efficient product that reduce energy consumption, save cost, and promote sustainability.</p>
    </div>
    <div class="abs col" style="left:591px">
      <h4>Products</h4>
      <ul><li>Heat pump</li><li>Air Conditioners</li><li>Swimming Pool Heat Pump</li><li>Monoblock Heat Pump</li></ul>
    </div>
    <div class="abs col" style="left:788px">
      <h4>Support</h4>
      <ul><li>Instructional Videos</li><li>System Documentation</li><li>Parts Manual</li><li>Term and Condition</li><li>Our Story</li></ul>
    </div>
    <div class="abs col" style="left:944px">
      <h4>Contacts</h4>
      <div class="contact-num">1800 555 014</div>
      <p>Information Request</p>
      <h4 style="margin-top:18px">Follow Us</h4>
      <div class="social" style="gap:8px"><span style="width:16px;height:16px"></span><span style="width:16px;height:16px"></span><span style="width:16px;height:16px"></span></div>
    </div>
    <div class="abs rule" style="top:364px;background:#333"></div>
    <div class="abs copy" style="top:386px">A OLVAK Company</div>
    <div class="abs copy" style="top:407px">Copyright 2024 OLVAK - All Right Reserved</div>
  </footer>

</div>
</body>
</html>
```